Business card and stationary for eco-aware technology company
Verdalux: Green-minded Scrap Recovery
Business card and stationary for eco-aware technology company - Chemicals
Creative Brief
Professional
Tam Brendow
Managing Director
7-3, 2nd Floor, Pelham Court, Quarry Road, 10450 Georgetown, Penang, Malaysia
+604-8XXXXXX
+6011-5274 XXXX
xxx@verdalux.example
http://www.verdalux.example
YYYYYYY-K
Hello, My name is Tam Brendow, and I am MD of Verdalux. I would like a letterhead and a business card for myself. Verdalux is a Malaysia-based startup with a focus on developing technology for urban mining ( http://scrapharvest.example/ ). Verdalux's name is legally Verdalux Sdn. Bhd., but maybe the shorter form, 'Verdalux' looks better on a business card. Perhaps the "Sdn. Bhd." could be hidden in there somewhere. Up to you! For the business card, the following info should be used: Tam Brendow Managing Director MChem, Ph.D (Chemistry) The back side of the business card can be blank, or it can be very simply decorated. I am on Malaysian time (GMT +8) so please forgive me if my feedback appears delayed. Thanks & good luck, - Tam
Empty is fine. Very simple decoration if you want - maybe just the company logo in the center.
tbrendow tbrendow
Hey, Sorry for the slow feedback. I've just got back to the office. Firstly, I am happy to review the business card designs on this site. However, the stationary designs are too big to preview and quorbasketch's site makes it too slow for me to look at the designs. So, would you designers be able to host the images on a web server, or put them in a .zip file? Private message me the URL and I'll download them and use an image viewer to see them offline. Sorry for the extra work - blame QS's crap design. Ok, now for some feedback: 1) The dark 'Eco' green does not look nice on the card. Please use only a little bit! 2) Lighter greens are nice. Like the colour of the 3 leaves. 3) No transparent cards, please. 4) The back of the card should have a very simple design. Maybe just the 3 leaves on a white background, with no text? 5) I love the designs with the big leaf (#191). It's clever. I also love the designs with the circuit pattern (#212, #213, #214). That's clever too. Private message me if you want more feedback or ideas. I'll try to reply fast. Thanks, - Tam

```html
<!DOCTYPE html>
<html lang="en">
<head>
<meta charset="utf-8">
<title>Verdalux business cards</title>
<link rel="stylesheet" href="https://fonts.googleapis.com/css2?family=Open+Sans:wght@400;600;700;800&display=swap">
<style>
  :root{
    --bg:#e9ebe9;
    --card:#ffffff;
    --green-dark:#13803a;
    --green:#2e9b43;
    --green-light:#8cc63f;
    --ink:#3a3a3a;
    --muted:#5d5d5d;
    --rule:#cfcfcf;
  }
  *{box-sizing:border-box;margin:0;padding:0}
  html,body{width:1200px;height:852px;overflow:hidden}
  body{background:var(--bg);font-family:"Open Sans",Arial,sans-serif;color:var(--ink);position:relative}
  .card{position:absolute;width:540px;height:309px;background:var(--card);border-radius:14px;overflow:hidden;box-shadow:0 6px 18px rgba(0,0,0,.18)}
  .card--primary{left:40px;top:110px}
  .card--alternate{left:620px;top:430px}
  .swoosh{position:absolute;left:0;bottom:0;width:540px;height:80px}
  .brand{display:flex;align-items:center;gap:10px}
  .brand-dot{width:46px;height:46px;border-radius:50%;background:var(--green-light)}
  .brand-name{font-weight:800;font-size:40px;line-height:1;color:var(--green)}
  .brand-tag{font-size:9.5px;letter-spacing:1.4px;text-transform:uppercase;color:var(--green);font-weight:600;margin-top:3px}
  .person-name{font-weight:700;font-size:15px;color:var(--green-dark)}
  .person-cred{font-weight:700;font-size:11px;color:var(--green)}
  .person-role{font-size:11.5px;color:var(--ink)}
  .address{font-size:10.5px;line-height:1.45;color:var(--muted)}
  .license{font-size:10.5px;color:var(--muted)}
  .contacts{list-style:none}
  .contacts li{display:flex;align-items:center;gap:7px;font-size:10.5px;color:var(--muted);height:17px}
  .contacts svg{width:11px;height:11px;flex:none}
  .divider{position:absolute;width:1px;background:var(--rule)}

  /* primary card */
  .card--primary .brand{position:absolute;left:78px;top:32px}
  .card--primary .person{position:absolute;left:60px;top:116px;width:210px;text-align:center}
  .card--primary .person .address{margin-top:12px}
  .card--primary .divider{left:292px;top:112px;height:112px}
  .card--primary .details{position:absolute;left:308px;top:108px}
  .card--primary .license{margin-bottom:5px}

  /* alternate card */
  .card--alternate .brand{position:absolute;left:30px;top:98px}
  .card--alternate .brand-dot{width:34px;height:34px}
  .card--alternate .brand-name{font-size:30px}
  .card--alternate .brand-tag{font-size:7.5px}
  .card--alternate .person{position:absolute;left:50px;top:156px;width:180px;text-align:left}
  .card--alternate .divider{left:252px;top:36px;height:180px}
  .card--alternate .details{position:absolute;left:268px;top:36px}
  .card--alternate .address{margin:4px 0 8px}
</style>
</head>
<body>

<svg width="0" height="0" style="position:absolute" aria-hidden="true">
  <defs>
    <symbol id="i-phone" viewBox="0 0 12 12"><path d="M2.5 1h2l1 2.6-1.3 1a6 6 0 0 0 3.2 3.2l1-1.3L11 7.5v2a1.5 1.5 0 0 1-1.5 1.5A8.5 8.5 0 0 1 1 2.5 1.5 1.5 0 0 1 2.5 1z" fill="#2e9b43"/></symbol>
    <symbol id="i-mobile" viewBox="0 0 12 12"><rect x="3" y="0.5" width="6" height="11" rx="1.2" fill="#2e9b43"/><rect x="4" y="2" width="4" height="7" fill="#fff"/></symbol>
    <symbol id="i-fax" viewBox="0 0 12 12"><rect x="3" y="1" width="6" height="4" fill="#2e9b43"/><rect x="0.5" y="4.5" width="11" height="5" rx="1" fill="#2e9b43"/><rect x="3" y="8" width="6" height="3.5" fill="#fff" stroke="#2e9b43"/></symbol>
    <symbol id="i-mail" viewBox="0 0 12 12"><rect x="0.5" y="2" width="11" height="8" rx="1" fill="#2e9b43"/><path d="M1 2.6 6 6.6l5-4" fill="none" stroke="#fff" stroke-width="1"/></symbol>
    <symbol id="i-web" viewBox="0 0 12 12"><circle cx="6" cy="6" r="5.3" fill="#2e9b43"/><path d="M0.8 6h10.4M6 0.8c-2.4 2.8-2.4 7.6 0 10.4M6 0.8c2.4 2.8 2.4 7.6 0 10.4" fill="none" stroke="#fff" stroke-width=".7"/></symbol>
    <symbol id="swoosh" viewBox="0 0 540 80" preserveAspectRatio="none">
      <path d="M0 48 C140 22 330 70 540 16 L540 80 L0 80 Z" fill="#13803a"/>
      <path d="M0 56 C150 32 340 76 540 28 L540 80 L0 80 Z" fill="#2e9b43"/>
      <path d="M0 40 C140 16 330 62 540 8" fill="none" stroke="#8cc63f" stroke-width="3"/>
    </symbol>
  </defs>
</svg>

<article class="card card--primary">
  <div class="brand">
    <span class="brand-dot"></span>
    <div>
      <div class="brand-name">Verdalux</div>
      <div class="brand-tag">Green-minded Scrap Recovery</div>
    </div>
  </div>
  <div class="person">
    <div class="person-name">Tam Brendow</div>
    <div class="person-cred">MChem, Ph.D (Chemistry)</div>
    <div class="person-role">Managing Director</div>
    <p class="address">7-3, 2nd Floor, Pelham Court,<br>Quarry Road, 10450 Georgetown<br>Penang, Malaysia</p>
  </div>
  <span class="divider"></span>
  <div class="details">
    <p class="license">License No 7058213-K</p>
    <ul class="contacts">
      <li><svg><use href="#i-phone"/></svg>604-8731906</li>
      <li><svg><use href="#i-mobile"/></svg>6011-5274 8063</li>
      <li><svg><use href="#i-fax"/></svg>604-8719342</li>
      <li><svg><use href="#i-mail"/></svg>info@verdalux.example</li>
      <li><svg><use href="#i-web"/></svg>www.verdalux.example</li>
    </ul>
  </div>
  <svg class="swoosh"><use href="#swoosh"/></svg>
</article>

<article class="card card--alternate">
  <div class="brand">
    <span class="brand-dot"></span>
    <div>
      <div class="brand-name">Verdalux</div>
      <div class="brand-tag">Green-minded Scrap Recovery</div>
    </div>
  </div>
  <div class="person">
    <div class="person-name">Tam Brendow</div>
    <div class="person-cred">MChem, Ph.D (Chemistry)</div>
    <div class="person-role">Managing Director</div>
  </div>
  <span class="divider"></span>
  <div class="details">
    <p class="license">License No 7058213-K</p>
    <p class="address">7-3, 2nd Floor, Pelham Court,<br>Quarry Road, 10450 Georgetown<br>Penang, Malaysia</p>
    <ul class="contacts">
      <li><svg><use href="#i-phone"/></svg>604-8731906</li>
      <li><svg><use href="#i-mobile"/></svg>6011-5274 8063</li>
      <li><svg><use href="#i-fax"/></svg>604-8719342</li>
      <li><svg><use href="#i-mail"/></svg>info@verdalux.example</li>
      <li><svg><use href="#i-web"/></svg>www.verdalux.example</li>
    </ul>
  </div>
  <svg class="swoosh"><use href="#swoosh"/></svg>
</article>

</body>
</html>
```